Sonstige Web-Design für Private Cloud Lösungen
Zielgruppe
Wir sind anbieter für Private Cloud Lösungen und benötigen eine Zeitgemäße Website, die ohne viel schnick schnack klar ausdrückt was wir machen.
Dabei die nötige Seriösität ausdrückt, welche hochsensible Daten benötigen.
Unsere Zielgruppe sind Unternehmen bis 250 MA
Die Farbgebung sollte an die des Logos angepasst sein, welches hier ebenfalls mit Farbcode hochgeladen wird.
Der Focus liegt auf Managed private Cloud und dem klaren kommitment Ihre Daten sicher in Deutschland
von der Landingpage soll es zur maximal 5 Unterseiten gehen.
1. Managed Private Cloud
2. Service Provider (Hier sollen unsere Dienstleistungen gelistet und auf einzelnen Seiten erklärt werden)
3. Trainings
4. Kontakt
Aufgabenstellung
Es sollte modern sein. Beim Besuch der Website soll auf der ersten Seite klar werden, was den Besucher erwartet jedoch ohne viel Worte.

```html
<!DOCTYPE html>
<html lang="de">
<head>
<meta charset="utf-8">
<title>Nordvia – Private-Cloud-Lösungen</title>
<link rel="stylesheet" href="https://fonts.googleapis.com/css2?family=Roboto:wght@400;500;700&display=swap">
<style>
  :root {
    --blue: #0e96cf;
    --ink: #ffffff;
    --dark: #2e2e2e;
    --card: #222222;
    --night: #05060c;
    --text-dark: #1d1d1d;
    --white: #ffffff;
  }
  * { margin: 0; padding: 0; box-sizing: border-box; }
  html, body { width: 1200px; height: 3234px; overflow: hidden; }
  body { font-family: "Roboto", Arial, sans-serif; color: var(--ink); background: var(--white); position: relative; }
  .abs { position: absolute; }

  /* Hero */
  .hero { position: absolute; left: 0; top: 0; width: 1200px; height: 674px; background: var(--night); overflow: hidden; }
  .hero-photo { position: absolute; inset: 0;
    background:
      radial-gradient(ellipse 280px 340px at 420px 330px, rgba(105,70,255,.85), rgba(60,30,200,.35) 55%, transparent 80%),
      linear-gradient(90deg, #6f7487 0%, #3b3f55 18%, #2a2260 32%, #120c33 55%, #05060c 75%); }
  .brand { left: 95px; top: 34px; height: 64px; display: flex; align-items: center; gap: 10px; }
  .brand-mark { width: 18px; height: 18px; border: 3px solid var(--blue); }
  .brand-name { font-size: 30px; font-weight: 700; color: var(--ink); letter-spacing: .5px; }
  .nav { top: 60px; left: 0; width: 1200px; font-size: 16px; font-weight: 500; }
  .nav a { position: absolute; color: var(--ink); text-decoration: none; white-space: nowrap; }
  .nav a.active { color: var(--blue); }
  .hero-title { left: 522px; top: 272px; font-size: 47px; font-weight: 700; line-height: 1.2; }
  .hero-text { left: 522px; top: 330px; width: 520px; font-size: 16px; font-weight: 500; line-height: 26px; }

  /* Partner strip */
  .partners { position: absolute; left: 0; top: 674px; width: 1200px; height: 167px; background: var(--white); }
  .partner { top: 62px; height: 44px; display: flex; align-items: center; gap: 10px; font-size: 26px; font-weight: 500; color: var(--text-dark); transform: translateX(-50%); white-space: nowrap; }
  .partner .dot { width: 22px; height: 22px; border-radius: 50%; background: #c7232f; }
  .partner.cloud { color: var(--blue); }
  .partner.cloud .dot { background: var(--blue); }
  .partner.team { color: #b03a2e; }
  .partner.team .dot { border-radius: 0; background: #b03a2e; }
  .badge { left: 875px; top: 58px; width: 220px; height: 56px; border: 2px solid #9a9a9a; border-radius: 4px; background: #f1f1f1; }

  /* Dark content */
  .content { position: absolute; left: 0; top: 841px; width: 1200px; height: 2078px; background: var(--dark); }
  .center { left: 0; width: 1200px; text-align: center; }
  .section-title { top: 93px; font-size: 35px; font-weight: 700; }
  .section-lead { top: 147px; font-size: 16px; font-weight: 500; line-height: 26px; }
  .card { top: 243px; width: 294px; height: 319px; background: var(--card); box-shadow: 0 0 22px rgba(0,0,0,.45); text-align: center; }
  .card svg { position: absolute; left: 107px; top: 20px; width: 80px; height: 82px; }
  .card h3 { position: absolute; top: 120px; left: 0; width: 100%; font-size: 28px; font-weight: 700; color: var(--blue); }
  .card p { position: absolute; top: 163px; left: 18px; right: 18px; font-size: 16px; font-weight: 500; line-height: 26px; }

  .feature-label { font-size: 16px; font-weight: 500; }
  .feature-title { font-size: 32px; font-weight: 700; line-height: 38px; }
  .feature-text { font-size: 16px; font-weight: 500; line-height: 26px; width: 420px; }
  .btn { display: flex; align-items: center; justify-content: center; width: 186px; height: 40px; border-radius: 5px; background: var(--blue); color: var(--white); font-size: 16px; font-weight: 700; text-decoration: none; }
  .photo { }
  .photo-reichstag { left: 607px; top: 727px; width: 408px; height: 271px; background: linear-gradient(180deg, #7aa3d4 0%, #b9cde6 45%, #8d8d8d 75%, #5d5d5d 100%); }
  .photo-datacenter { left: 95px; top: 1166px; width: 411px; height: 270px; background: linear-gradient(180deg, #3d4a60 0%, #1e2430 45%, #c9d3df 70%, #e6ebf1 100%); }
  .photo-training { left: 607px; top: 1644px; width: 411px; height: 270px; background: linear-gradient(160deg, #c9c3b4 0%, #7a6a5a 40%, #3a2e26 75%, #6b5647 100%); }

  /* CTA */
  .cta { position: absolute; left: 0; top: 2919px; width: 1200px; height: 315px; background: var(--white); }
  .cta-title { top: 66px; font-size: 47px; font-weight: 700; color: var(--blue); }
  .cta-text { top: 132px; font-size: 16px; font-weight: 500; line-height: 26px; color: var(--text-dark); }
  .cta-btn { left: 395px; top: 203px; width: 410px; height: 59px; border-radius: 6px; font-size: 22px; }
</style>
</head>
<body>

<header class="hero">
  <div class="hero-photo" role="img" aria-label="Foto: IT-Techniker arbeitet am Laptop im blau beleuchteten Rechenzentrum"></div>
  <div class="abs brand"><span class="brand-mark"></span><span class="brand-name">Nordvia</span></div>
  <nav class="abs nav">
    <a class="active" style="left:463px">Start</a>
    <a style="left:545px">Managed Privat Cloud</a>
    <a style="left:759px">Service Provider</a>
    <a style="left:931px">Trainings</a>
    <a style="left:1045px">Kontakt</a>
  </nav>
  <h1 class="abs hero-title">Private-Cloud-Lösungen</h1>
  <p class="abs hero-text">Lorem ipsum dolor sit amet, consectetuer adipiscing elit Aenean com modo ligula eget dolor. Aenean massa. Cum sociis natoque penatibus et magen piscing elit ligula eget dolor.</p>
</header>

<section class="partners">
  <div class="abs partner" style="left:210px"><span class="dot"></span>Schildwerk</div>
  <div class="abs partner cloud" style="left:423px"><span class="dot"></span>Wolkenhaus</div>
  <div class="abs partner team" style="left:684px"><span class="dot"></span>Teamfeld</div>
  <div class="abs badge" aria-label="Partner-Abzeichen"></div>
</section>

<main class="content">
  <h2 class="abs center section-title">Schöpfen Sie Ihr volles Potenzial aus.</h2>
  <p class="abs center section-lead">Lorem ipsum dolor sit amet, consectetuer adipiscing elit Aenean com modo ligula eget<br>dolor. Aenean massa. Cum sociis natoque penatibus escing elit ligula eget dolor.</p>

  <article class="abs card" style="left:112px">
    <svg viewBox="0 0 80 82" fill="none" stroke="#0e96cf" stroke-width="5">
      <path d="M4 80V16M4 80h72"/>
      <rect x="14" y="40" width="8" height="38" fill="#0e96cf" stroke="none"/>
      <rect x="28" y="52" width="8" height="26" fill="#0e96cf" stroke="none"/>
      <rect x="42" y="60" width="8" height="18" fill="#0e96cf" stroke="none"/>
      <circle cx="46" cy="26" r="13" stroke-width="4"/>
      <path d="M52 20c-5-4-11-1-11 6s6 10 11 6M38 24h10M38 29h10" stroke-width="3"/>
      <path d="M60 40l14 14M74 44v10H64" stroke-width="4"/>
    </svg>
    <h3>Kosten senken</h3>
    <p>Aenean com modo ligula eget dolor. Aenean massa. Cum sociis natoque pena tibus escing elit ligula eget dolor.</p>
  </article>

  <article class="abs card" style="left:453px">
    <svg viewBox="0 0 80 82" fill="none" stroke="#0e96cf" stroke-width="4">
      <path d="M22 4v44M40 4v44M58 4v44"/>
      <rect x="16" y="14" width="12" height="8" fill="#0e96cf"/>
      <rect x="34" y="28" width="12" height="8" fill="#0e96cf"/>
      <rect x="52" y="18" width="12" height="8" fill="#0e96cf"/>
      <path d="M4 58h10v20H4z" fill="#0e96cf"/>
      <path d="M14 62c8-4 16-4 24 0h14c4 0 4 6 0 6H36M14 76c10 4 22 4 34-2l24-14c4-2 6 2 3 5L52 80" stroke-width="5"/>
    </svg>
    <h3>Mehr Kontrolle</h3>
    <p>Lorem ipsum dolor sit amet, conse ctetuer adipiscing elit Aenean com modo ligula eget dolor. Aenean massa.</p>
  </article>

  <article class="abs card" style="left:794px">
    <svg viewBox="0 0 80 82" fill="none" stroke="#0e96cf" stroke-width="3.5">
      <ellipse cx="40" cy="6" rx="9" ry="4"/><path d="M31 6v14c0 5 18 5 18 0V6M31 13c0 5 18 5 18 0"/>
      <ellipse cx="10" cy="30" rx="8" ry="3.5"/><path d="M2 30v12c0 5 16 5 16 0V30M2 36c0 5 16 5 16 0"/>
      <ellipse cx="70" cy="30" rx="8" ry="3.5"/><path d="M62 30v12c0 5 16 5 16 0V30M62 36c0 5 16 5 16 0"/>
      <ellipse cx="40" cy="62" rx="9" ry="4"/><path d="M31 62v14c0 5 18 5 18 0V62M31 69c0 5 18 5 18 0"/>
      <path d="M40 24v30M22 38h12M46 38h12M34 46l6 8 6-8"/>
    </svg>
    <h3>Leichter Skalieren</h3>
    <p>Lorem ipsum dolor sit amet, conse ctetuer adipiscing elit Aenean com modo ligula eget dolor. Aenean massa.</p>
  </article>

  <!-- Managed Privat Cloud -->
  <p class="abs feature-label" style="left:95px;top:729px">Managed Privat Cloud</p>
  <h2 class="abs feature-title" style="left:95px;top:757px">Ihre Daten in Deutschland</h2>
  <p class="abs feature-text" style="left:95px;top:810px">Lorem ipsum dolor sit amet, consectetuer adipiscing elit Aenean com modo ligula eget dolor. Aenean massa. Cum sociis natoque penatibus escing elit ligula eget dolor.</p>
  <a class="abs btn" style="left:95px;top:932px">Zum Überblick</a>
  <div class="abs photo photo-reichstag" role="img" aria-label="Foto: Deutschlandflagge vor einem historischen Parlamentsgebäude"></div>

  <!-- Service Provider -->
  <div class="abs photo photo-datacenter" role="img" aria-label="Foto: Serverraum eines Rechenzentrums mit Racks und Kabeltrassen"></div>
  <p class="abs feature-label" style="left:607px;top:1170px">Service Provider</p>
  <h2 class="abs feature-title" style="left:607px;top:1198px">Der Full Service Provider<br>für den Mittelstand</h2>
  <p class="abs feature-text" style="left:607px;top:1288px">Lorem ipsum dolor sit amet, consectetuer adipiscing elit Aenean com modo ligula eget dolor. Aenean massa. Cum sociis natoque penatibus escing elit ligula eget dolor.</p>
  <a class="abs btn" style="left:609px;top:1404px">Zum Überblick</a>

  <!-- Trainings -->
  <p class="abs feature-label" style="left:95px;top:1635px">Trainings</p>
  <h2 class="abs feature-title" style="left:95px;top:1666px">IT-Training für Unter-<br>nehmen - Wir bringen Sie<br>weiter</h2>
  <p class="abs feature-text" style="left:95px;top:1794px">Lorem ipsum dolor sit amet, consectetuer adipiscing elit Aenean com modo ligula eget dolor. Aenean massa. Cum sociis natoque penatibus escing elit ligula eget dolor.</p>
  <a class="abs btn" style="left:95px;top:1914px">Zum Überblick</a>
  <div class="abs photo photo-training" role="img" aria-label="Foto: Schulungsraum mit Teilnehmenden an Laptops und Trainer"></div>
</main>

<section class="cta">
  <h2 class="abs center cta-title">Sie möchten mehr erfahren?</h2>
  <p class="abs center cta-text">Lorem ipsum dolor sit amet, consectetuer adipiscing elit Aenean com modo ligula eget<br>dolor. Aenean massa. Cum sociis natoque penatibus escing elit ligula eget dolor.</p>
  <a class="abs btn cta-btn">Mit einem Experten sprechen</a>
</section>

</body>
</html>
```